Manual design

Hello,

I am looking for someone creative to help me design my Real Estate related manual. I am looking for something simple yet impressive. It would be designed around my logo and brand colors and I would also like it to have a local feel, perhaps with photos I could provide of my area/hometown. I am really shooting for an impressive company and branded look, while keeping it neat without too much going on.

I have the content that I would like to include, I am just struggling with the design of the manual in general.

I have attached a copy of my logo, my companys logo, and a publisher file of what I had previously done. Please do not think the design I previously used is something to work off of if you deem it better to use another feel. I am looking for originality, unless you can improve upon my old file. Any questions, please feel free to reach out to me.

The content in the provided brochure will remain the same, it is the design aspect I need help with. Thanks

Target Market(s)

My target market is home sellers aged 25-55, people usually selling their 1st or second home

Industry/Entity Type

Real Estate

Requirements
Must have
• -A simple to read design focused around my logo and colors
-A local sense
Should not have
• Drawings, only real photos

```html
<!DOCTYPE html>
<html lang="en">
<head>
<meta charset="utf-8">
<title>Educated Seller's Guide – Dalen Gorsky</title>
<link href="https://fonts.googleapis.com/css2?family=Roboto:wght@300;400;700&display=swap" rel="stylesheet">
<style>
:root{
  --navy:#0b2566;
  --navy-2:#1f4b9c;
  --panel:#8a95c8;
  --panel-2:#aab2da;
  --bar:#5d74b8;
  --paper:#ffffff;
  --bg:#f1f1f1;
  --ink:#1b2a55;
  --rule:#d4d4d4;
}
*{box-sizing:border-box;margin:0;padding:0}
html,body{width:1200px;height:677px;overflow:hidden;background:var(--bg);font-family:"Roboto",Arial,sans-serif;color:#fff}
.page{position:absolute;width:362px;height:288px;background:var(--paper);border:1px solid var(--rule);box-shadow:0 1px 3px rgba(0,0,0,.12);overflow:hidden}
.p1{left:30px;top:38px}.p2{left:415px;top:38px}.p3{left:800px;top:38px}
.p4{left:30px;top:345px}.p5{left:415px;top:345px}.p6{left:800px;top:345px}

.brand{position:absolute;left:10px;top:10px;display:flex;flex-direction:column;align-items:center;gap:2px}
.brand .dot{width:14px;height:14px;border-radius:50%;background:var(--navy)}
.brand .name{font-weight:700;font-size:8.5px;line-height:9px;color:var(--navy);text-align:center;letter-spacing:.3px}
.agent{position:absolute;right:12px;top:8px;display:flex;flex-direction:column;align-items:center;gap:2px}
.agent .sq{width:30px;height:24px;background:var(--navy)}
.agent .url{font-size:7px;font-weight:700;color:var(--navy)}

.band{position:absolute;left:0;right:0;top:67px;height:207px;background:linear-gradient(90deg,var(--navy) 0%,var(--navy-2) 100%)}
.photo{position:absolute}
.ph-tower{background:linear-gradient(160deg,#7fa9dc 0%,#dfe6ee 50%,#8e9b7c 100%)}
.ph-skyline{background:linear-gradient(180deg,#9cc0e6 0%,#d8e4f0 60%,#5f6e7e 100%)}
.ph-map{background:linear-gradient(160deg,#5e86c7 0%,#24427f 100%)}
.ph-person{background:linear-gradient(180deg,#6e8fb0 0%,#c4a98e 100%)}
.ph-office{background:linear-gradient(160deg,#9a9a9a 0%,#d8d3c8 100%)}
.ph-brick{background:linear-gradient(180deg,#cfdbea 0%,#a6674e 55%,#7a4a38 100%)}
.ph-glass{background:linear-gradient(170deg,#cfe1f3 0%,#6f8fb4 100%)}
.ph-home{background:linear-gradient(180deg,#8fb7e6 0%,#e8dcc0 55%,#5b8a4c 100%)}

.quote{position:absolute;background:linear-gradient(180deg,var(--panel) 0%,var(--panel-2) 100%);color:#fff;font-size:7px;line-height:9px;text-align:right;padding:10px 8px}
.quote .by{display:block;margin-top:8px}
.pnum{position:absolute;right:10px;bottom:2px;font-size:11px;color:var(--ink);font-weight:300}

h1.title{position:absolute;font-weight:300;color:#fff;font-size:21px;line-height:24px}
h1.cover-title{left:0;width:218px;top:145px;text-align:right;font-size:17px;line-height:20px}
.body{position:absolute;font-size:6.2px;line-height:7.6px;color:#fff}
.body p{margin-bottom:6px}
.body b{font-weight:700}

.cover-agent{position:absolute;right:44px;bottom:20px;text-align:right;font-size:5.5px;line-height:7px;color:#fff}
.cover-badge{position:absolute;right:6px;bottom:14px;display:flex;flex-direction:column;align-items:center;gap:1px}
.cover-badge .sq{width:30px;height:22px;background:var(--navy)}
.cover-badge .url{font-size:7px;font-weight:700;color:var(--navy)}

.toc{position:absolute;left:28px;top:92px;width:172px;font-size:6.3px;line-height:11.6px}
.toc li{list-style:none;display:flex;justify-content:space-between;color:#cfd7f0}
.toc-rule{position:absolute;left:210px;top:67px;width:1px;height:207px;background:rgba(255,255,255,.35)}

.chart{position:absolute}
.stat-label{font-size:5.6px;fill:#fff;font-family:"Roboto",Arial,sans-serif}
.stat-row{font-size:4.8px;fill:#fff;font-family:"Roboto",Arial,sans-serif}
.stat-val{font-size:11px;fill:#fff;font-weight:300;font-family:"Roboto",Arial,sans-serif}
.note{position:absolute;font-size:5px;color:#fff}
.power{position:absolute;color:#fff}
.power h2{font-weight:300;font-size:14px;line-height:15px}
.power p{font-weight:700;font-size:7.5px;line-height:9px}
.badge-shape{position:absolute;width:16px;height:16px;border-radius:50%;background:#fff}
</style>
</head>
<body>

<section class="page p1">
  <div class="brand"><span class="dot"></span><span class="name">HARBOURLINE<br>REALTY</span></div>
  <div class="band" style="width:226px"></div>
  <div class="photo ph-tower" style="left:226px;top:67px;width:136px;height:108px" role="img" aria-label="Photo of modern residential towers with palm trees"></div>
  <div class="photo ph-skyline" style="left:0;top:175px;width:226px;height:99px" role="img" aria-label="Photo of a city skyline"></div>
  <div class="quote" style="left:226px;top:175px;width:136px;height:99px"></div>
  <h1 class="title cover-title">Educated Seller's Guide</h1>
  <div class="cover-agent">DALEN GORSKY<br>Multi-Award Winning<br>Real Estate Professional<br>604-555-0142<br>homes@gorsky.ca</div>
  <div class="cover-badge"><span class="sq"></span><span class="url">gorsky.ca</span></div>
</section>

<section class="page p2">
  <div class="brand"><span class="dot"></span><span class="name">HARBOURLINE<br>REALTY</span></div>
  <div class="agent"><span class="sq"></span><span class="url">gorsky.ca</span></div>
  <div class="band"></div>
  <div class="toc-rule"></div>
  <h1 class="title" style="left:28px;top:70px;font-size:17px">Content</h1>
  <ul class="toc">
    <li><span>Meet Dalen Gorsky</span><span>1</span></li>
    <li><span>About Harbourline Realty</span><span>2</span></li>
    <li><span>How to Qualify A Real Estate Professional</span><span>3</span></li>
    <li><span>How I Can Help You</span><span>4</span></li>
    <li><span>Where Do Buyers Come From</span><span>6</span></li>
    <li><span>Marketing Systems</span><span>7</span></li>
    <li><span>Intelligent Home Pricing</span><span>9</span></li>
    <li><span>Your Exclusive Entitlements</span><span>10</span></li>
    <li><span>Preparing Your Home for Sale</span><span>11</span></li>
    <li><span>Keys to Successful Showings</span><span>12</span></li>
    <li><span>Exclusive Easy Exit Guarantee</span><span>13</span></li>
    <li><span>A Few Words from Clients</span><span>14</span></li>
    <li><span>Forms to Prepare in Advance</span><span>15</span></li>
  </ul>
  <div class="photo ph-tower" style="left:226px;top:67px;width:136px;height:108px" role="img" aria-label="Photo of modern residential towers"></div>
  <div class="quote" style="left:226px;top:175px;width:136px;height:99px;padding-top:18px">“First comes thought; then organization of that thought, into ideas and plans; then transformation of those plans into reality. The beginning, as you will observe, is in your imagination.”<span class="by">- Nathan Hale-Brook</span></div>
</section>

<section class="page p3">
  <div class="brand"><span class="dot"></span><span class="name">HARBOURLINE<br>REALTY</span></div>
  <div class="agent"><span class="sq"></span><span class="url">gorsky.ca</span></div>
  <div class="band"></div>
  <h1 class="title" style="left:10px;top:70px;font-size:16px">Meet Dalen Gorsky</h1>
  <div class="body" style="left:10px;top:93px;width:270px">
    <p>First and foremost, thank you for your time and the opportunity to wow you. Since 2007, I have been looking for the most progressive and innovative ways to help my clients succeed. The traditional model of real estate sales has been slowly dying in the last decade as we have seen radical changes in our industry and economy. A time when being a real estate professional meant putting a sign in the yard and being the gate keeper of information is long ago dead, and a new era of Real Estate sales is upon us. You don't just have to be good, you have to be really good to survive in this business. <b>The first step is the way you treat people. The second, is simply results.</b></p>
    <p>Coming from a customer service and business background running a multi-million dollar per year business as head management, I knew that Real Estate sales would be the perfect fit to expand my future. I began in Real Estate in 2007 coming from training with a top selling Real Estate team, producing almost 10 times what the average Realtor maintains each year. Once I got my feet wet, I launched into a program with Marcus Hale Intl., a professional coaching company, being trained by some of the countries top Real Estate professionals. <b>Each and every week, I connect and train with successful, like-minded business experts to learn how to better serve my customers and business.</b> This has allowed me to produce extraordinary results.</p>
    <p>I am a simple man. I enjoy snowboarding on my days off, sip-ping on new craft beers when relaxing, and enjoying quality time with my family and dog. When I am not working, I am reading books by bril-liant people who have been gracious enough to leave their life's under-standings and experiences in writing for me to devour. I cherish my personal time as much as I cherish my business and helping people move forward with their ambitions. <b>This is who I am, and I am grateful and humbled to be able to serve you..</b></p>
  </div>
  <div class="photo ph-person" style="left:285px;top:67px;width:77px;height:55px" role="img" aria-label="Portrait photo of the agent"></div>
  <div class="photo ph-office" style="left:285px;top:124px;width:77px;height:66px" role="img" aria-label="Photo of the agent receiving an award"></div>
  <div class="quote" style="left:285px;top:190px;width:77px;height:84px;padding-top:24px">“Don't wish it was easier, wish you were better.”<span class="by">- Jon Rowan</span></div>
  <span class="pnum">1</span>
</section>

<section class="page p4">
  <div class="brand"><span class="dot"></span><span class="name">HARBOURLINE<br>REALTY</span></div>
  <div class="band"></div>
  <h1 class="title" style="left:10px;top:70px;font-size:16px">About Harbourline Realty</h1>
  <div class="body" style="left:10px;top:92px;width:200px">
    <p>A locally owned, full-service real estate company serving BC families <b>since 1944</b>. A trusted name in Real Estate.</p>
    <p>Founded in 1944 on Vancouver's West Side, Harbourline Realty is a locally owned company with <b>20 offices and nearly 1,000 sales professionals</b> throughout British Columbia. Unlike most brokerage firms, Harbourline Realty is a true full-service real estate company with divisions in residential sales, commercial sales and leasing, property management, project marketing, and mortgage services.</p>
    <p>With a <b>gross sales volume of $4.7 Billion</b> in 2009, Harbourline Realty is Western Canada's largest real estate brokerage firm, beating out Summit Homes, Crown Realty, Keystone, and Meridian office on the West Coast.</p>
  </div>
  <span class="badge-shape" style="left:10px;top:200px"></span>
  <div class="body" style="left:10px;top:228px;width:200px">
    <p><b>Harbourline Realty is a member of the Premier Realty Alliance Worldwide</b> network, through which we are affiliated with over 145,000 sales associates in 600+ top real estate firms across North America and in 30+ countries around the world.</p>
  </div>
  <div class="photo ph-map" style="left:215px;top:67px;width:147px;height:63px" role="img" aria-label="Map of British Columbia office locations"></div>
  <div class="quote" style="left:215px;top:130px;width:147px;height:144px;font-size:6.6px;line-height:8px;padding:12px 14px 0 10px">“Again, you can't connect the dots looking forward; you can only connect them looking backwards. So you have to trust that the dots will somehow connect in your future. You have to trust in something - your gut, destiny, life, karma, what-ever. This approach has never let me down, and it has made all the difference in my life.”<span class="by">- Stan Jorvik</span></div>
  <span class="pnum">2</span>
</section>

<section class="page p5">
  <div class="brand"><span class="dot"></span><span class="name">HARBOURLINE<br>REALTY</span></div>
  <div class="agent"><span class="sq"></span><span class="url">gorsky.ca</span></div>
  <div class="band"></div>
  <h1 class="title" style="left:10px;top:74px;font-size:15px;line-height:15px">How to qualify a<br>real estate professional</h1>
  <div class="body" style="left:10px;top:108px;width:200px">
    <p>Questions <b>all</b> Real Estate sales professionals should be able to answer:</p>
    <p>1. How many homes did you sell last year?<br>2. What are you percentage of homes that are selling?<br>3. What is your average list to sales price ratio vs. the average for the market?<br>4. What is your average marketing time vs. the MLS average marketing time?<br>5. Do you have a list of past clients I can call?<br>6. Do you follow up on all showings and will you give me feedback?<br>7. Do you have a copy of the Realtor Code of Ethics?<br>8. How much money do you spend each year on education and sales training?<br>9. Are you full time?</p>
  </div>
  <div class="quote" style="left:215px;top:67px;width:147px;height:68px;text-align:center;padding-top:8px">“I believe that if you show people the problems and you show them the solutions they will be moved to act.”<span class="by" style="text-align:right">- Bill Garrity</span></div>
  <div class="photo ph-brick" style="left:215px;top:135px;width:147px;height:80px" role="img" aria-label="Photo of a modern brick condominium building"></div>
  <div class="quote" style="left:215px;top:215px;width:147px;height:59px;padding:0"></div>
  <div class="power" style="left:221px;top:219px;width:136px">
    <h2>POWER THOUGHT:</h2>
    <p>Hire the professional who is best qualified to handle your most valuable asset, your home.</p>
  </div>
  <span class="pnum">3</span>
</section>

<section class="page p6">
  <div class="brand"><span class="dot"></span><span class="name">HARBOURLINE<br>REALTY</span></div>
  <div class="agent"><span class="sq"></span><span class="url">gorsky.ca</span></div>
  <div class="band"></div>
  <h1 class="title" style="left:10px;top:70px;font-size:16px">How I Can Help You</h1>
  <div class="body" style="left:10px;top:92px;width:225px"><p>My goal is to sell your home for the most amount of money, in the shortest period of time. So how do I compare to other Realtors out there...?</p></div>
  <svg class="chart" style="left:0;top:108px" width="240" height="140" viewBox="0 0 240 140">
    <text class="stat-label" x="48" y="12">Average Days on Market</text>
    <text class="stat-row" x="45" y="25" text-anchor="end">Dalen Gorsky</text>
    <rect x="48" y="18" width="38" height="10" fill="var(--bar)"/>
    <text class="stat-val" x="66" y="27.5">35</text>
    <text class="stat-row" x="45" y="41" text-anchor="end">VCREB average</text>
    <rect x="48" y="34" width="62" height="10" fill="var(--bar)"/>
    <text class="stat-val" x="92" y="43.5">57</text>
    <text class="stat-label" x="48" y="63">% of List Price Achieved</text>
    <text class="stat-label" x="48" y="71">for Listings</text>
    <text class="stat-row" x="45" y="89" text-anchor="end">Dalen Gorsky</text>
    <rect x="48" y="81" width="78" height="11" fill="var(--bar)"/>
    <text class="stat-val" x="91" y="91">99,40%</text>
    <text class="stat-row" x="45" y="104" text-anchor="end">VCREB average</text>
    <rect x="48" y="96" width="56" height="11" fill="var(--bar)"/>
    <text class="stat-val" x="55" y="106">96,51%</text>
    <path d="M120 94 Q126 112 112 124" stroke="#fff" stroke-width="1" stroke-dasharray="2 2" fill="none"/>
    <text class="stat-label" x="58" y="130" style="font-weight:700">Additional 2,89%</text>
    <text class="stat-label" x="140" y="12">Less days on market means:</text>
    <text class="stat-label" x="140" y="20">• Less showings and time away</text>
    <text class="stat-label" x="144" y="27">from home.</text>
    <text class="stat-label" x="140" y="34">• Less strangers in your home.</text>
    <text class="stat-label" x="140" y="41">• Less cleaning.</text>
    <text class="stat-label" x="140" y="63">Multiply 2.89% by your estimat-</text>
    <text class="stat-label" x="140" y="70">ed sale price to determine to ad-</text>
    <text class="stat-label" x="140" y="77">ditional amount that I will negoti-</text>
    <text class="stat-label" x="140" y="84">ate for you.</text>
    <text class="stat-label" x="140" y="98">2.89 x $200,000= $5,790</text>
    <text class="stat-label" x="140" y="105">2.89 x $350,000= $7,311</text>
    <text class="stat-label" x="140" y="112">2.89 x 550,000= $15,895</text>
    <text class="stat-label" x="140" y="119">2.89 x 750,000= $21,675</text>
  </svg>
  <div class="photo ph-glass" style="left:245px;top:67px;width:117px;height:68px" role="img" aria-label="Photo of a glass office building"></div>
  <div class="quote" style="left:245px;top:135px;width:117px;height:68px;padding-top:12px;font-weight:700;font-size:6.2px;line-height:7.6px">“Remember, if you ever need a helping hand, it's at the end of your arm, as you get older, remember you have another hand: The first is to help yourself, the second is to help others.”<span class="by" style="font-weight:400;margin-top:5px">- Audra Hemsley</span></div>
  <div class="photo ph-home" style="left:245px;top:203px;width:117px;height:71px" role="img" aria-label="Photo of a suburban home with palm trees"></div>
  <span class="note" style="left:110px;top:266px">*Statistics provided by the Valley Coast Real Estate Board</span>
  <span class="pnum">4</span>
</section>

</body>
</html>
```